the theater production needs a poster design

we need a poster design for a theater drama in Seoul , South Korea.

the title : THE LANTERN KEEPER'S ROAD
BASED ON WALTER DREVICK'S BOOK

where:Haneulbit Stagehouse, Jongro-Gu, Seoul
when:2022.1.1~OpenRun
Saturday 3PM, 63PM, Sunday 5pm, Monday 7:30pm

TICKET PRICE: $45

BOOK NOW
02 471 6039
RIVA TROUPE

Director Minha Park Composer Sora Lee, Sound Director Doyun Han
Producer Taesik Yoon

Target Market(s)

for Chiristan and others

Industry/Entity Type

Christian community and non Christian society

Colors
0094D4
00A9DD
6FCCEA
C7EBF8
E9F6FB

Requirements
Must have
• the main Character, pilgrim should should carry some burdens on his shoulder

```html
<!DOCTYPE html>
<html lang="en">
<head>
<meta charset="utf-8">
<title>The Lantern Keeper's Road — Theatre Poster</title>
<link rel="stylesheet" href="https://fonts.googleapis.com/css2?family=Cinzel:wght@400;500&family=Oswald:wght@300;400;500;600&display=swap">
<style>
  :root {
    --backdrop: #252525;
    --paper: #ffffff;
    --ink: #0d0d0d;
    --ink-soft: #1e1e1e;
    --night: #0a0a0a;
    --light-text: #ffffff;
    --accent-red: #e8252a;
  }
  * { margin: 0; padding: 0; box-sizing: border-box; }
  html, body {
    width: 1200px; height: 1200px; overflow: hidden;
    background: var(--backdrop);
  }
  .poster {
    position: absolute; left: 168px; top: 23px;
    width: 865px; height: 1153px;
    background: var(--paper);
    overflow: hidden;
    font-family: 'Oswald', sans-serif;
    color: var(--ink);
  }
  .scene-photo {
    position: absolute; left: 0; right: 0; top: 620px; bottom: 0;
    background: linear-gradient(to bottom,
      rgba(255,255,255,0) 0%,
      #f2f2f2 18%,
      #c9c9c9 38%,
      #6a6a6a 58%,
      #2a2a2a 74%,
      var(--night) 90%);
  }
  .source-line {
    position: absolute; top: 62px; left: 0; right: 0;
    text-align: center;
    font-weight: 600; font-size: 28px; letter-spacing: 5px;
  }
  .title {
    position: absolute; top: 150px; left: 0; right: 0;
    text-align: center;
    font-family: 'Cinzel', serif; font-weight: 400;
    line-height: 1;
  }
  .title span { display: block; }
  .title .line-one { font-size: 86px; }
  .title .line-two { font-size: 124px; margin-top: 14px; }
  .title .line-three { font-size: 118px; margin-top: 10px; }
  .credits {
    position: absolute; top: 520px; left: 0; right: 0;
    text-align: center;
  }
  .credit { margin-bottom: 31px; }
  .credit-role {
    font-weight: 600; font-size: 23px; letter-spacing: 0.5px;
    line-height: 30px;
  }
  .credit-name {
    font-weight: 300; font-size: 24px; line-height: 32px;
    color: var(--ink-soft);
  }
  .run-dates {
    position: absolute; left: 67px; top: 938px;
    color: var(--light-text);
    font-weight: 300; font-size: 29px; letter-spacing: 2px;
  }
  .schedule {
    position: absolute; left: 67px; top: 978px;
    color: var(--light-text);
    font-weight: 600; font-size: 27px; letter-spacing: 3px;
    line-height: 30px;
  }
  .icon-calendar { position: absolute; left: 34px; top: 982px; width: 26px; height: 26px; }
  .icon-pin { position: absolute; left: 38px; top: 1075px; width: 18px; height: 24px; }
  .venue {
    position: absolute; left: 67px; top: 1076px;
    color: var(--light-text);
    font-weight: 400; font-size: 17px; letter-spacing: 2px;
  }
  .ticket-price {
    position: absolute; right: 52px; top: 858px;
    color: var(--light-text);
    font-weight: 600; font-style: italic; font-size: 25px; letter-spacing: 3px;
  }
  .booking {
    position: absolute; right: 55px; top: 930px;
    width: 140px; text-align: center;
    color: var(--light-text);
  }
  .booking-call {
    font-weight: 600; font-size: 62px; line-height: 56px; letter-spacing: 6px;
    margin-right: -6px;
  }
  .booking-phone {
    display: block; margin-top: 6px;
    background: var(--accent-red);
    font-weight: 500; font-size: 19px; letter-spacing: 2px; line-height: 24px;
  }
  .company-name {
    font-weight: 400; font-size: 20px; letter-spacing: 2px; margin-top: 3px;
  }
</style>
</head>
<body>
  <main class="poster">
    <div class="scene-photo" role="img" aria-label="Misty black and white road with bare trees, a lone pilgrim walking into the fog and a flock of birds in the sky"></div>

    <p class="source-line">BASED ON WALTER DREVICK'S BOOK</p>

    <h1 class="title">
      <span class="line-one">THE LANTERN</span>
      <span class="line-two">KEEPER'S</span>
      <span class="line-three">ROAD</span>
    </h1>

    <section class="credits">
      <div class="credit">
        <p class="credit-role">DIRECTOR</p>
        <p class="credit-name">Minha Park Composer Sora Lee</p>
      </div>
      <div class="credit">
        <p class="credit-role">SOUND DIRECTOR</p>
        <p class="credit-name">Doyun Han</p>
      </div>
      <div class="credit">
        <p class="credit-role">PRODUCER</p>
        <p class="credit-name">Taesik Yoon</p>
      </div>
    </section>

    <p class="run-dates">2022.1.1~OpenRun</p>

    <svg class="icon-calendar" viewBox="0 0 26 26" aria-hidden="true">
      <rect x="1.5" y="3.5" width="18" height="16" rx="2" fill="none" stroke="#e8252a" stroke-width="2"/>
      <rect x="1.5" y="3.5" width="18" height="4" fill="#e8252a"/>
      <line x1="6" y1="1" x2="6" y2="5" stroke="#e8252a" stroke-width="2"/>
      <line x1="15" y1="1" x2="15" y2="5" stroke="#e8252a" stroke-width="2"/>
      <rect x="4" y="10" width="3" height="2.5" fill="#e8252a"/>
      <rect x="9" y="10" width="3" height="2.5" fill="#e8252a"/>
      <rect x="4" y="14" width="3" height="2.5" fill="#e8252a"/>
      <circle cx="19" cy="19" r="6" fill="#0a0a0a" stroke="#e8252a" stroke-width="2"/>
      <path d="M19 16 V19 H21.5" fill="none" stroke="#e8252a" stroke-width="1.8"/>
    </svg>

    <p class="schedule">
      SATURDAY 3PM, 6:30PM<br>
      SUNDAY 5PM<br>
      MONDAY 7:30PM
    </p>

    <svg class="icon-pin" viewBox="0 0 18 24" aria-hidden="true">
      <path d="M9 1 C4.5 1 1 4.5 1 9 C1 15 9 23 9 23 C9 23 17 15 17 9 C17 4.5 13.5 1 9 1 Z" fill="#e8252a"/>
      <circle cx="9" cy="9" r="3.2" fill="#0a0a0a"/>
    </svg>
    <p class="venue">HANEULBIT STAGEHOUSE, JONGRO-GU, SEOUL</p>

    <p class="ticket-price">TICKET PRICE: $45</p>

    <div class="booking">
      <p class="booking-call">BOOK<br>NOW</p>
      <span class="booking-phone">02 471 6039</span>
      <p class="company-name">RIVA TROUPE</p>
    </div>
  </main>
</body>
</html>
```